mno School poster design and change logo name

We already have a logo which only needs to be slightly modified with "school".
We also have two advertising faces, a girl and a boy, which should be on our poster.
Important key data:

bilingual D/E small classes
daycare
private kindergarten
private school from 2024

Poster size: 268,5 x 128 cm
We need logo sizes in different sizes
also for T-shirts.
Attached also a old poster

Target Market(s)

new clients

Colors
0094D4
00A9DD
6FCCEA
C7EBF8
E9F6FB
59FF00
82FF00
B8FF75
E3FFCB
F4FFEA
FFC000
F8CF3A
FAE287
FDF2CF
FEFAEE
F0912C
F2A743
F7CA91
FBE8D2
FDF5EE

```html
<!DOCTYPE html>
<html lang="en">
<head>
<meta charset="utf-8">
<title>mno School Banner</title>
<link rel="stylesheet" href="https://fonts.googleapis.com/css2?family=Source+Serif+4:wght@400;600;700&family=Montserrat:wght@400;500&display=swap">
<style>
  :root {
    --page: #c9c9c9;
    --orange: #e0431d;
    --orange-light: #ea5a28;
    --blue: #0a74a8;
    --blue-light: #1489bf;
    --accent-blue: #0a6fb0;
    --tab: #55463f;
    --white: #ffffff;
    --ink: #222222;
    --red-rule: #d8362a;
    --logo-orange: #f0912c;
  }
  * { margin: 0; padding: 0; box-sizing: border-box; }
  html, body { width: 1200px; height: 651px; overflow: hidden; background: var(--page); }
  .stage { position: relative; width: 1200px; height: 651px; }
  .banner {
    position: absolute; left: 0; top: 39px;
    width: 1312px; height: 626px;
    transform: scale(0.9146); transform-origin: 0 0;
    background: var(--white); overflow: hidden;
    font-family: "Source Serif 4", Georgia, serif;
  }
  .hero {
    position: absolute; left: 0; top: 0; width: 1312px; height: 441px;
    background: linear-gradient(90deg, var(--orange) 0%, var(--orange-light) 100%);
  }
  .headline {
    position: absolute; left: 52px; top: 34px;
    color: var(--white); font-weight: 700; font-size: 72px; line-height: 84px; letter-spacing: -0.5px;
  }
  .divider { position: absolute; left: 58px; top: 212px; width: 644px; height: 2px; background: var(--white); }
  .divider-accent { position: absolute; left: 92px; top: 210px; width: 138px; height: 6px; background: var(--accent-blue); border-radius: 2px; }
  .subline {
    position: absolute; left: 57px; top: 238px;
    color: var(--white); font-size: 31px; line-height: 42px; font-weight: 400;
  }
  .photo { position: absolute; left: 740px; top: 0; width: 572px; height: 441px; }
  .tab { position: absolute; left: 456px; top: 368px; width: 320px; height: 73px; }
  .tab-text {
    position: absolute; right: 600px; top: 374px; text-align: right;
    color: var(--white); font-size: 16px; line-height: 20px; font-weight: 600;
  }
  .band {
    position: absolute; left: 0; top: 441px; width: 1312px; height: 106px;
    background: linear-gradient(90deg, var(--blue) 0%, var(--blue-light) 100%);
  }
  .offer {
    position: absolute; top: 458px; height: 72px;
    border: 1.5px solid var(--white); border-radius: 8px;
    display: flex; align-items: center; justify-content: center; text-align: center;
    color: var(--white); font-size: 24px; line-height: 27px;
  }
  .logo-disc {
    position: absolute; left: 46px; top: 380px; width: 280px; height: 280px;
    border-radius: 50%; background: var(--white);
  }
  .logo-name {
    position: absolute; left: 46px; top: 490px; width: 280px; text-align: center;
    color: var(--logo-orange); font-weight: 700; font-size: 46px; line-height: 56px;
  }
  .contact {
    position: absolute; left: 380px; top: 547px; height: 79px; right: 30px;
    display: flex; align-items: center; gap: 16px;
    font-family: "Montserrat", Arial, sans-serif; color: var(--ink); white-space: nowrap;
  }
  .phone { font-size: 29px; }
  .web, .address { font-size: 19px; }
  .sep { display: block; width: 2px; height: 32px; background: var(--red-rule); flex: none; }
</style>
</head>
<body>
<div class="stage">
  <div class="banner">
    <div class="hero"></div>

    <h1 class="headline">Give your child<br>the best start in life!</h1>
    <div class="divider"></div>
    <div class="divider-accent"></div>
    <p class="subline">The bilingual all-day care from the crèche<br>to the private all-day kindergarten.</p>

    <svg class="photo" viewBox="0 0 572 441" role="img" aria-label="Photo of a smiling girl holding up paint-covered hands">
      <defs>
        <radialGradient id="photoTone" cx="0.55" cy="0.55" r="0.55">
          <stop offset="0" stop-color="#f2c3a4"/>
          <stop offset="0.6" stop-color="#d98a5c"/>
          <stop offset="1" stop-color="#e4481f" stop-opacity="0"/>
        </radialGradient>
      </defs>
      <rect width="572" height="441" fill="url(#photoTone)"/>
    </svg>

    <svg class="tab" viewBox="0 0 320 73" aria-hidden="true">
      <path d="M20 0 H320 L300 73 H0 Z" fill="var(--tab)"/>
    </svg>
    <p class="tab-text">Kinderkrippe &amp; Hort<br>Ab3. Lebensmonat<br>bis zun 12.Lebenesjahr</p>

    <div class="band"></div>
    <div class="offer" style="left:387px;width:182px;">Bilingual D/E<br>small classes</div>
    <div class="offer" style="left:586px;width:187px;">Day Care</div>
    <div class="offer" style="left:795px;width:266px;">Private kindergarten</div>
    <div class="offer" style="left:1078px;width:187px;">Private school<br>from 2024</div>

    <div class="contact">
      <span class="phone">+41 791234567</span>
      <i class="sep"></i>
      <span class="web">www.mno-daycare.ch</span>
      <i class="sep"></i>
      <span class="address">Lindenweg 12 8000 Musterdorf</span>
    </div>

    <div class="logo-disc"></div>
    <div class="logo-name">mno School</div>
  </div>
</div>
</body>
</html>
```